We are having a Bright Dawn, Bold Self Reshape Challenge at our fitness studio. We need a poster design using the template attached as a reference. I have also included our Vorabloom logo to put on the poster. Please DO NOT use the graphics in the flyer as we are expecting something much better :-)

-Size needed 11x17 with bleeding for printing

-We need this made in Photoshop (CS3 friendly) or at least delivered in PS as we might change some text or re-arrange the design later on.

-We need this in layers.

```html
<!DOCTYPE html>
<html lang="en">
<head>
<meta charset="utf-8">
<title>Bright Dawn, Bold Self Reshape Challenge — Vorabloom Bootcamps</title>
<link rel="stylesheet" href="https://fonts.googleapis.com/css2?family=Bevan&family=Orbitron:wght@900&family=Oswald:wght@500;700&display=swap">
<style>
  :root {
    --paper: #ffffff;
    --wine-deep: #2e0505;
    --wine: #5a0c0c;
    --wine-glow: #9a1a16;
    --title-yellow: #f6e619;
    --accent-orange: #e2781f;
    --rule-orange: #c9601c;
    --ribbon: #8e2a26;
    --ribbon-dark: #5e1512;
    --ink: #111111;
    --white: #ffffff;
  }
  * { box-sizing: border-box; margin: 0; padding: 0; }
  html, body { width: 800px; height: 1200px; overflow: hidden; background: var(--paper); }
  .poster { position: relative; width: 800px; height: 1200px; background: var(--paper); }
  .poster-field {
    position: absolute; left: 33px; top: 33px; width: 734px; height: 1134px; overflow: hidden;
    background:
      repeating-linear-gradient(90deg, rgba(0,0,0,0.12) 0 2px, transparent 2px 7px),
      linear-gradient(180deg, var(--wine-deep) 0%, var(--wine) 45%, var(--wine-deep) 100%);
  }
  .athlete-photo {
    position: absolute; left: 80px; top: 420px; width: 560px; height: 640px;
    background: radial-gradient(ellipse at 50% 45%, rgba(154,26,22,0.85) 0%, rgba(110,18,16,0.5) 45%, transparent 72%);
  }
  .lifter-figure {
    position: absolute; top: 170px; width: 75px; height: 110px;
    background: radial-gradient(ellipse, rgba(140,30,26,0.75) 0%, transparent 70%);
  }
  .lifter-figure--left { left: 108px; }
  .lifter-figure--right { left: 518px; }

  .brand-plate {
    position: absolute; left: 239px; top: 53px; width: 322px; height: 117px;
    background: var(--white); border: 2px solid var(--ink);
    display: flex; align-items: center; justify-content: center;
  }
  .brand-name {
    font-family: "Bevan", serif; font-size: 30px; color: var(--ink);
    line-height: 1.05; text-align: center; letter-spacing: 1px;
  }

  .contest-title {
    position: absolute; left: 0; width: 800px; text-align: center;
    font-family: "Orbitron", sans-serif; font-weight: 900; color: var(--title-yellow);
  }
  .contest-title--l1 { top: 196px; font-size: 38px; }
  .contest-title--l2 { top: 238px; font-size: 38px; }
  .contest-title--l3 { top: 290px; font-size: 34px; }
  .contest-label {
    position: absolute; left: 0; width: 800px; top: 342px; text-align: center;
    font-family: "Orbitron", sans-serif; font-weight: 900; font-size: 15px; color: var(--white); letter-spacing: 1px;
  }

  .slant-band { position: absolute; left: 0; top: 0; width: 800px; height: 1200px; }
  .slant-text {
    position: absolute; font-family: "Bevan", serif; color: var(--white);
    white-space: nowrap; transform: rotate(-5.3deg); transform-origin: center;
  }
  .slant-text--l1 { left: 262px; top: 383px; font-size: 36px; letter-spacing: 2px; }
  .slant-text--l2 { left: 110px; top: 432px; font-size: 36px; letter-spacing: 2px; }

  .headline-joiner {
    position: absolute; left: 0; width: 800px; top: 510px; text-align: center;
    font-family: "Orbitron", sans-serif; font-weight: 900; font-size: 17px; color: var(--white);
  }
  .headline {
    position: absolute; left: 0; width: 800px; text-align: center;
    font-family: "Oswald", sans-serif; font-weight: 700; color: var(--white);
    text-transform: uppercase; line-height: 1;
  }
  .headline--l1 { top: 542px; font-size: 70px; }
  .headline--l2 { top: 614px; font-size: 58px; }
  .headline--l3 { top: 672px; font-size: 50px; }

  .rule { position: absolute; left: 33px; width: 734px; height: 2px; background: var(--rule-orange); }
  .rule--top { top: 736px; }
  .rule--bottom { top: 862px; }

  .schedule { position: absolute; left: 184px; font-family: "Oswald", sans-serif; font-weight: 700; color: var(--accent-orange); white-space: nowrap; line-height: 1; }
  .schedule--kickoff { top: 745px; font-size: 19px; }
  .schedule--start { top: 780px; font-size: 27px; }
  .schedule--end { top: 820px; font-size: 27px; }
  .schedule sup { font-size: 12px; vertical-align: 12px; }

  .offer { position: absolute; left: 187px; font-family: "Oswald", sans-serif; font-weight: 700; color: var(--white); white-space: nowrap; line-height: 1; text-transform: uppercase; }
  .offer--l1 { top: 893px; font-size: 41px; }
  .offer--l2 { top: 942px; font-size: 35px; }
  .offer--l3 { top: 983px; font-size: 41px; }

  .prize-ribbon { position: absolute; left: 0; top: 0; width: 800px; height: 1200px; }
  .prize-text {
    position: absolute; left: 190px; top: 1075px; width: 420px; text-align: center;
    font-family: "Bevan", serif; font-size: 19px; color: var(--white); letter-spacing: 1px;
    transform: rotate(-5.3deg); white-space: nowrap;
  }
</style>
</head>
<body>
<main class="poster">
  <div class="poster-field">
    <div class="athlete-photo" role="img" aria-label="Red-toned photo of a muscular athlete behind the headline"></div>
    <div class="lifter-figure lifter-figure--left" role="img" aria-label="Silhouette of a weightlifter"></div>
    <div class="lifter-figure lifter-figure--right" role="img" aria-label="Silhouette of a woman lifting dumbbells"></div>
  </div>

  <div class="brand-plate"><span class="brand-name">VORABLOOM<br>BOOTCAMPS</span></div>

  <h1>
    <span class="contest-title contest-title--l1">BRIGHT DAWN,</span>
    <span class="contest-title contest-title--l2">BOLD SELF</span>
    <span class="contest-title contest-title--l3">RESHAPE</span>
  </h1>
  <p class="contest-label">CHALLENGE</p>

  <svg class="slant-band" viewBox="0 0 800 1200" aria-hidden="true">
    <line x1="33" y1="418" x2="767" y2="350" stroke="#ffffff" stroke-width="3"/>
    <line x1="33" y1="528" x2="767" y2="458" stroke="#ffffff" stroke-width="3"/>
  </svg>
  <p class="slant-text slant-text--l1">IN JUST 6 WEEKS,</p>
  <p class="slant-text slant-text--l2">TRANSFORM YOUR BODY</p>

  <p class="headline-joiner">And</p>
  <h2>
    <span class="headline headline--l1">Get in the</span>
    <span class="headline headline--l2">Best Shape</span>
    <span class="headline headline--l3">of your life!</span>
  </h2>

  <div class="rule rule--top"></div>
  <p class="schedule schedule--kickoff">KICK OFF MEETING : Thursday, Jan 14 at 7:30 pm</p>
  <p class="schedule schedule--start">START DATE : Monday, January 18<sup>th</sup></p>
  <p class="schedule schedule--end">END DATE : Friday, February 26<sup>th</sup></p>
  <div class="rule rule--bottom"></div>

  <p class="offer offer--l1">6 weeks of training,</p>
  <p class="offer offer--l2">nutrition and coaching</p>
  <p class="offer offer--l3">starting at just $99!</p>

  <svg class="prize-ribbon" viewBox="0 0 800 1200" aria-hidden="true">
    <polygon points="33,1033 200,1050 200,1100 33,1098" fill="var(--ribbon-dark)"/>
    <polygon points="600,1028 767,1010 767,1078 600,1080" fill="var(--ribbon-dark)"/>
    <polygon points="180,1085 615,1043 615,1088 180,1128" fill="var(--ribbon)"/>
  </svg>
  <p class="prize-text">$500 CASH PRIZE FOR WINNER!</p>
</main>
</body>
</html>
```